Marlow Institute Counsellor iPhone app design

Live wireframes are here;

https://view.plankora.example/7c2e91a04d6b3f8e5a1c9d0b2e4f6a8c3d5e7f90#/pages/48210935

Password - marlowinst482!

We're nearing completion of the Blueprinting phase for our app development project for Marlow Institute. We need a designs matching the attached functional specification we've created for the app.

VISION
The Marlow Institute Counselling Services app provides simple and accessible information and engagement with mobile relevant services.
Opening the app, users are greeted with a simple “Hello, how are you today?” a 3 multiple choice answers to both aid in contextual content presentation/navigation specific to the users needs.
Users can access a range of existing web resources from the current website via live in app content and web links. Users can also access a personal folder storing PDF’s that are shared as part of meetings with Marlow Counsellors.
The app also features evolving content pulling from the existing WIKI and presents new and user relevant updates upon opening the app.
Finally, the solution will also deliver support to senior counsellors on each campus by streamlining tasks (such as booking appointments etc). The solution will also provide counsellors with notifications on students at risk and who may need greater support on their journeys.

Target Market(s)

People aged 15 to 24 years
• Students in this age group represent the largest market for
the industry, accounting for an estimated 44.7% of industry revenue in 2014-15. Demand for vocational education from school leavers has declined, as government reforms in higher education have led to more available university places for undergraduate students. Consequently, this market has declined in its share of revenue over the past five years.

People aged 25 to 44 years
• People aged 25 to 44 years are estimated to account for
37.2% of industry revenue. This market has grown its share of revenue over the past five years, as many Australians are entering the system to retrain or update workforce skills due to structural changes occurring in the economy. Students in this age group typically work full- time and therefore undertake their studies part-time, either on-campus or through distance learning.

People aged 45 years and over
• Individuals in this market represent 18.1% of the industry.
The majority of students in this age group have well- established careers, so students undertaking vocational courses are either seeking to upskill or have decided to change careers. As many of these students are employed full-time and often have family commitments, they require more flexible class schedules. This market has remained relatively stable as a share of revenue over the past five years.

Industry/Entity Type

Counsellor

Font styles to use
Sans Serif

Requirements
Must have
• The app needs to meet accessibility guidelines, so no text in images, nice flat design etc.
• The wireframes attached are not to spec, they're just a guide.
• Designs must meet the Apple interface guidelines and device specs for iPhone 4s, 5, 5s, 6 6+
• We also need an app store logo.
Nice to have
• NA

```html
<!DOCTYPE html>
<html lang="en">
<head>
<meta charset="utf-8">
<title>Marlow Counsellors – Home</title>
<link rel="stylesheet" href="https://fonts.googleapis.com/css2?family=Arimo:wght@700&family=Cabin:wght@500&family=Raleway:wght@300;400&display=swap">
<style>
  :root {
    --page-bg: #eeeeee;
    --bar-black: #0d0d0d;
    --nav-black: #121212;
    --white: #ffffff;
    --text-soft: #f3efe6;
    --panel: rgba(150, 130, 100, 0.28);
    --blue: #2f86e0;
    --yellow: #e9d13a;
    --red: #c93a06;
    --tab-top: #3a3a3a;
    --tab-bottom: #1c1c1c;
    --tab-active: #0f0f0f;
    --tab-divider: #121212;
  }
  * { box-sizing: border-box; margin: 0; padding: 0; }
  html, body { width: 960px; height: 1200px; overflow: hidden; background: var(--page-bg); }
  .screen {
    position: absolute; left: 101px; top: 30px; width: 757px; height: 1139px;
    background: var(--bar-black); overflow: hidden;
  }
  .status-bar {
    height: 50px; background: var(--bar-black); color: #e6e6e6;
    font-family: "Arimo", Arial, sans-serif; font-weight: 700; font-size: 29px;
    position: relative;
  }
  .status-bar .carrier { position: absolute; left: 10px; top: 8px; display: flex; align-items: center; gap: 12px; }
  .status-bar .time { position: absolute; left: 0; right: 0; top: 8px; text-align: center; }
  .status-bar .battery { position: absolute; right: 10px; top: 14px; }
  .nav-bar {
    height: 106px; background: var(--nav-black); position: relative;
    display: flex; align-items: center; justify-content: center;
  }
  .nav-title { font-family: "Cabin", sans-serif; font-weight: 500; font-size: 34px; color: var(--white); }
  .back-button { position: absolute; left: 15px; top: 25px; }
  .menu-button { position: absolute; right: 18px; top: 40px; }
  .hero {
    position: absolute; left: 0; top: 156px; width: 757px; height: 859px;
    background:
      radial-gradient(ellipse 45% 30% at 75% 18%, rgba(190,150,70,0.85), transparent 70%),
      radial-gradient(ellipse 40% 30% at 20% 12%, rgba(170,170,140,0.8), transparent 70%),
      radial-gradient(ellipse 50% 35% at 55% 25%, rgba(140,90,35,0.8), transparent 75%),
      linear-gradient(180deg, #8c7a55 0%, #6b4e2a 35%, #3e2a16 60%, #261710 100%);
  }
  .welcome {
    position: absolute; left: 0; right: 0; top: 196px; text-align: center;
    font-family: "Raleway", sans-serif; font-weight: 300; font-size: 31px; color: var(--text-soft);
  }
  .choices {
    position: absolute; left: 18px; top: 307px; width: 719px; height: 346px;
    background: var(--panel); display: flex; justify-content: space-around; padding: 0 30px;
  }
  .choice { width: 200px; text-align: center; padding-top: 63px; }
  .choice svg { display: block; margin: 0 auto; }
  .choice-label {
    margin-top: 19px; font-family: "Raleway", sans-serif; font-weight: 400; font-size: 20px; color: var(--text-soft);
  }
  .tab-bar {
    position: absolute; left: 0; top: 1015px; width: 757px; height: 124px;
    display: flex; background: linear-gradient(var(--tab-top), var(--tab-bottom));
  }
  .tab {
    flex: 1; display: flex; flex-direction: column; align-items: center; justify-content: flex-start;
    padding-top: 20px; border-right: 2px solid var(--tab-divider);
    font-family: "Raleway", sans-serif; font-size: 19px; color: var(--white);
  }
  .tab:last-child { border-right: none; }
  .tab.active { background: var(--tab-active); }
  .tab svg { height: 56px; margin-bottom: 4px; }
</style>
</head>
<body>
<main class="screen">
  <header class="status-bar">
    <div class="carrier">Carrier
      <svg width="36" height="28" viewBox="0 0 36 28"><path d="M2 10a23 23 0 0 1 32 0M7 15a16 16 0 0 1 22 0M12 20a9 9 0 0 1 12 0" stroke="#e6e6e6" stroke-width="4" fill="none" stroke-linecap="round"/><circle cx="18" cy="25" r="3" fill="#e6e6e6"/></svg>
    </div>
    <div class="time">11:31 AM</div>
    <svg class="battery" width="50" height="24" viewBox="0 0 50 24"><rect x="1.5" y="1.5" width="42" height="21" rx="3" fill="none" stroke="#e6e6e6" stroke-width="3"/><rect x="5" y="5" width="35" height="14" fill="#e6e6e6"/><rect x="45" y="8" width="4" height="8" fill="#e6e6e6"/></svg>
  </header>
  <nav class="nav-bar">
    <svg class="back-button" width="110" height="58" viewBox="0 0 110 58">
      <path d="M18 2H104a4 4 0 0 1 4 4V52a4 4 0 0 1-4 4H18L2 29Z" fill="#141414" stroke="#bdbdbd" stroke-width="1.5"/>
      <text x="60" y="37" text-anchor="middle" font-family="Cabin, sans-serif" font-size="22" fill="#fff">Back</text>
    </svg>
    <h1 class="nav-title">Marlow Counsellors</h1>
    <svg class="menu-button" width="40" height="24" viewBox="0 0 40 24"><path d="M0 2H40M0 12H40M0 22H40" stroke="#fff" stroke-width="2.5"/></svg>
  </nav>
  <section class="hero" role="img" aria-label="Softly blurred warm photograph of a calm campus interior">
    <p class="welcome">Welcome to Marlow Counselling, how can we help?</p>
    <div class="choices">
      <div class="choice">
        <svg width="168" height="168" viewBox="-84 -84 168 168" aria-hidden="true">
          <circle r="84" fill="#fff"/>
          <polygon points="27.6,-66.5 66.5,-27.6 66.5,27.6 27.6,66.5 -27.6,66.5 -66.5,27.6 -66.5,-27.6 -27.6,-66.5" fill="var(--blue)"/>
          <path d="M0-20c15 0 27 8 27 18S15 16 0 16c-4 0-7 0-10-1l-12 8 3-11c-5-4-8-8-8-14 0-10 12-18 27-18z" fill="none" stroke="#fff" stroke-width="3.5" stroke-linejoin="round"/>
        </svg>
        <p class="choice-label">Talk to someone</p>
      </div>
      <div class="choice">
        <svg width="168" height="168" viewBox="-84 -84 168 168" aria-hidden="true">
          <circle r="84" fill="#fff"/>
          <polygon points="27.6,-66.5 66.5,-27.6 66.5,27.6 27.6,66.5 -27.6,66.5 -66.5,27.6 -66.5,-27.6 -27.6,-66.5" fill="var(--yellow)"/>
          <rect x="-27" y="-21" width="54" height="42" fill="none" stroke="#fff" stroke-width="4"/>
          <rect x="-19" y="-13" width="38" height="6" fill="#fff"/>
          <rect x="-19" y="-2" width="15" height="15" fill="#fff"/>
          <path d="M0 0H19M0 6H19M0 12H19" stroke="#fff" stroke-width="3"/>
        </svg>
        <p class="choice-label">Read Articles</p>
      </div>
      <div class="choice">
        <svg width="168" height="168" viewBox="-84 -84 168 168" aria-hidden="true">
          <circle r="84" fill="#fff"/>
          <polygon points="27.6,-66.5 66.5,-27.6 66.5,27.6 27.6,66.5 -27.6,66.5 -66.5,27.6 -66.5,-27.6 -27.6,-66.5" fill="var(--red)"/>
          <path d="M-28 12L10-24 24 14Z" fill="#fff"/>
          <path d="M-8 16a7 7 0 0 0 14 2" fill="none" stroke="#fff" stroke-width="4"/>
        </svg>
        <p class="choice-label">Blog</p>
      </div>
    </div>
  </section>
  <footer class="tab-bar">
    <div class="tab">
      <svg viewBox="0 0 56 56" width="56"><path d="M4 28L28 6 52 28" fill="none" stroke="#fff" stroke-width="5" stroke-linejoin="round"/><path d="M11 27V50H45V27L28 12Z" fill="#fff"/><rect x="24" y="36" width="9" height="14" fill="#2a2a2a"/><rect x="39" y="8" width="6" height="12" fill="#fff"/></svg>
      Home
    </div>
    <div class="tab">
      <svg viewBox="0 0 56 56" width="56"><rect x="5" y="8" width="46" height="40" fill="none" stroke="#fff" stroke-width="4"/><rect x="11" y="14" width="34" height="5" fill="#fff"/><rect x="11" y="23" width="14" height="18" fill="#fff"/><path d="M29 25H45M29 31H45M29 37H45" stroke="#fff" stroke-width="3"/></svg>
      Articles
    </div>
    <div class="tab">
      <svg viewBox="0 0 56 56" width="56"><path d="M4 24L28 8 52 24V48H4Z" fill="#fff"/><path d="M4 24L28 40 52 24" fill="none" stroke="#2a2a2a" stroke-width="2.5"/><rect x="15" y="17" width="26" height="14" fill="#2a2a2a"/><path d="M20 22H36M20 27H36" stroke="#fff" stroke-width="2"/></svg>
      Contacts
    </div>
    <div class="tab">
      <svg viewBox="0 0 56 56" width="56"><rect x="7" y="11" width="42" height="37" rx="3" fill="none" stroke="#fff" stroke-width="4"/><rect x="22" y="6" width="12" height="9" fill="#fff"/><circle cx="21" cy="26" r="5" fill="#fff"/><path d="M13 41a8 8 0 0 1 16 0Z" fill="#fff"/><path d="M32 26H43M32 32H43M32 38H43" stroke="#fff" stroke-width="3"/></svg>
      Profile
    </div>
    <div class="tab active">
      <svg viewBox="0 0 56 56" width="56"><circle cx="28" cy="28" r="23" fill="#fff"/><circle cx="30" cy="17" r="4" fill="#111"/><path d="M23 26H32L28 40H33" fill="none" stroke="#111" stroke-width="5" stroke-linejoin="round"/></svg>
      About
    </div>
  </footer>
</main>
</body>
</html>
```